We are a new company with 2 divisions a medical research and medical product sales. We need a company logo and Business Cards. The design files need to be provided to us in Adobe Photoshop CS 5.1.

Target Market(s)

Medical Community

Industry/Entity Type

Medical

Contact Information for Business Card

Company Name - Larkmoor Biomedical LLC
Company Address 4217 NE 14th Ave Suite 7, Gainesville Fl 32609

Requirements
Must have
• The design files need to be provided to us in Adobe Photoshop CS 5.1.

```html
<!DOCTYPE html>
<html lang="en">
<head>
<meta charset="utf-8">
<title>Larkmoor Biomedical LLC – Business Card</title>
<link rel="stylesheet" href="https://fonts.googleapis.com/css2?family=Sorts+Mill+Goudy&display=swap">
<style>
  :root {
    --backdrop: #e9e7e2;
    --card-light: #f4f9e6;
    --card-mid: #dcedae;
    --card-lime: #c3dc6c;
    --band-green: #11532c;
    --brand-green: #1d7a3a;
    --mark-green: #7fbf3e;
    --ink: #1c2b1c;
  }
  * { margin: 0; padding: 0; box-sizing: border-box; }
  html, body {
    width: 1200px;
    height: 900px;
    overflow: hidden;
    background: var(--backdrop);
  }
  .canvas {
    position: relative;
    width: 1200px;
    height: 900px;
  }
  .business-card {
    position: absolute;
    left: 180px;
    top: 210px;
    width: 840px;
    height: 480px;
    overflow: hidden;
    background: linear-gradient(100deg, var(--card-light) 0%, var(--card-mid) 45%, var(--card-lime) 100%);
    box-shadow: 0 6px 18px rgba(0, 0, 0, 0.18);
    font-family: "Sorts Mill Goudy", "Goudy Old Style", Georgia, serif;
  }
  .brand-band {
    position: absolute;
    left: 0;
    top: 0;
  }
  .company-name {
    position: absolute;
    left: 52px;
    top: 282px;
    color: var(--brand-green);
    font-size: 36px;
    line-height: 38px;
    text-transform: uppercase;
    letter-spacing: 0.5px;
    font-weight: 400;
  }
  .person {
    position: absolute;
    right: 140px;
    top: 118px;
    text-align: right;
    color: var(--brand-green);
  }
  .person-name {
    font-size: 32px;
    line-height: 34px;
    font-weight: 400;
    letter-spacing: 0.5px;
  }
  .person-title {
    font-size: 21px;
    line-height: 24px;
    color: var(--band-green);
  }
  .contact {
    position: absolute;
    right: 48px;
    top: 300px;
    text-align: right;
    color: var(--ink);
    font-size: 21px;
    line-height: 25px;
    font-style: normal;
  }
</style>
</head>
<body>
<main class="canvas">
  <article class="business-card">
    <svg class="brand-band" width="840" height="480" viewBox="0 0 840 480" aria-hidden="true">
      <path d="M118 0 H258 V150 A74 74 0 0 0 118 150 Z" fill="var(--band-green)"/>
      <circle cx="188" cy="200" r="66" fill="var(--mark-green)"/>
    </svg>
    <h1 class="company-name">Larkmoor<br>Biomedical LLC.</h1>
    <div class="person">
      <p class="person-name">JOHN DOE</p>
      <p class="person-title">Chief Executive Officer</p>
    </div>
    <address class="contact">
      4217 NE 14th Ave Suite 7,<br>
      Gainesville Fl 32609<br>
      Phone: 123 456 789<br>
      Email: yourname@yourcompany.com<br>
      www.yourcompany.com
    </address>
  </article>
</main>
</body>
</html>
```